Ferrobay | Minimalist 6-panel Brochure

Background: Ferro Bay Fabricators Corp. is a manufacturer of steel wire-based products (e.g. nails, galvanized wire, barbed wire, steel matting) in Manila.

Brand Differentiator: Uncompromising "first world" quality to push our "third world" country to develop

Customers: We are a B2B company - we supply the materials to be used by Contractors in building projects. Retailers in selling to home users,Wholesalers in distributing to their retailer networks.

Brochure Objective: Using a standard 6-panel 8.5" x 11" Brochure, to create awareness among contractors and in the architectural community as a leader in quality products and honest service. (architects are big influencers of contractors in that they can recommend quality suppliers to them)

Brochure Contents: I have attached (in Powerpoint) the copy points of the Brochures broken down by 6 panels of content.
**DO NOT MIND how I've layout-ed the info in the .ppt, It's for your easier understanding only**

Brand Essence to Consider: 'First-world' in terms of product standards. Transparent & honest in terms of service/delivery. Approachable from Big to Small customers.

*Bonus Brand Essence: Someone you can have a 'light' conversation with over the phone for a quotation.*

Design Guidelines:
1) Be creative. If you think any of the guidelines I mention below won't be the best fit to your interpretation of my vision, go ahead and do what you think is best!

2) Be minimalist. I've kept the copy points's words at a minimum so there would be more emphasis on the content. Design around the copy points that bring out the gist more and the details less.

3) Design flat. Make the design look simple yet attractive.
PEG: If there was a website that I'd like to take design cues from, it's www.plinthory.com and tovelink.com/purse . Details like font size, font color, etc here were nicely differentiated for Headers, Subtexts and Descriptions. Be playful with using font effects like BOLD and Italics.

4) Use Icons. Instead of using a photo-heavy brochure, it would be better if we created icons for the brochure parts ('Our Thinking', 'How We Serve You', 'How It Works')
PEG: Abstract/minimalist icons such as those seen at the top of quellmarks.com or the middle section of inkvardle.com would be nice.

5) Edit the Product Shots and Pics of our Tech/Machines. Kindly edit and 'beautify' the photos attached to align to your design. Use 1 shot per product. Some are in .jpeg and some in .psd. (see attached. remove the watermarks in .psd shots)

6) Fit the Logo. Feel free to change to color schemes of our logo to make it fit with your designs. (see attached)

7) Front Cover. Kindly go through our 'Tagline' and 'Short Overall Description' first to find inspiration for some simple artwork.
*sidenote: For you to understand our tagline, the Philippines hasn't fully developed a priority for quality in terms of steel materials used in construction. (price had always dictated the market) And we want to help push them to that point in shaping the country's real estate development from 3rd world to a 1st world country's standards.

8) Word Cloud. I've listed 8 of the biggest and well-known projects we've supported in the past 5 years in 'Supported Projects' and my idea is for you to create a nice 'Word Cloud' of it similar to how I presented it in the ppt attached. Or it can be presented in some shape you'd think is nice. (search "word cloud" in Zendro Pictures)

9) Call-to-Action. Make the 'Call-to-Action' panel of the brochure as "inviting" as possible.

10) Be creative. AGAIN. Aside for the copy points in the ppt guidelines attached, I would like to stress that you are free to edit/create whatever you deem fit to my vision. (as you've come to know what I'd like by now)

Don't forget to have fun!! It'll be awesome working with you.

**UPDATE in July 24: Use the PPT v2 for details, attached separately. (now with design pegs)**

**UPDATE in July 29: for the photos under 'First World Tech', please use the Cutter photo and Wire-drawing machine photo attached here.**
Updates

Hello again! Good job so far on the initial designs. To let you know what style I'd like our icons in "How We Serve You", please visit www.ferrobayph.sitevane.com for our mock-up website.

You can also scroll down in the first page in "Our 4 Products" to see how I'd like our fonts to be used here so it'll be readable (i.e. through different font sizes, font effects like Bold & Italic)

As always, if you think you have a better idea on how to execute what I've mentioned above, go do it!

**UPDATE in July 24: Use the PPT v2 for the copy details, attached separately. Now with Design PEGS.**

Reason: extending for a few more days for last-minute submissions/revisions. Thanks!

Target Market(s)

Architectural firms. Building contractors. Steel wholesalers/distributors.

Industry/Entity Type

Real Estate

Requirements
Must have
• Simple. Approachable. Clear. Attractive. Uncluttered.
Should not have
• BULLET POINTS. (this shouldn't look like a Powerpoint material in any way or form)

```html
<!DOCTYPE html>
<html lang="en">
<head>
<meta charset="utf-8">
<title>Ferrobay Brochure – Inside Panels</title>
<link href="https://fonts.googleapis.com/css2?family=Bebas+Neue&family=Open+Sans:ital,wght@0,400;0,600;0,700;1,700&display=swap" rel="stylesheet">
<style>
:root{
  --teal:#0b8dbd;
  --ink:#3e4955;
  --text:#2e2e2e;
  --muted:#555;
  --marker:#8e9499;
  --bg:#ffffff;
}
*{margin:0;padding:0;box-sizing:border-box}
html,body{width:1200px;height:1000px;overflow:hidden;background:var(--bg)}
body{font-family:"Open Sans",Arial,sans-serif;color:var(--text);position:relative}
.abs{position:absolute}
.band{position:absolute;left:0;width:1200px;height:14px}
.band-top{top:79px}
.band-bottom{top:904px}
.marker{position:absolute;width:22px;height:46px}
.section-title{position:absolute;font-family:"Bebas Neue",Impact,sans-serif;color:var(--teal);font-size:34px;letter-spacing:.3px;line-height:1}
.lead{left:27px;top:156px;width:366px;text-align:center;font-size:22.5px;line-height:31px;color:#3a3a3a}
.value{left:27px;width:370px;font-size:13px;line-height:16px}
.value b{color:var(--teal);font-weight:700}
.serve-icon{position:absolute;left:27px;width:74px;height:76px}
.serve-title{position:absolute;left:119px;font-size:17.5px;font-weight:700;color:#222}
.serve-text{position:absolute;left:119px;width:270px;font-size:14.5px;line-height:20.5px;color:#333}
.product-shot{position:absolute;left:427px;width:136px;height:102px;border-radius:1px}
.product{position:absolute;left:576px;width:206px}
.product-name{font-family:"Bebas Neue",Impact,sans-serif;font-size:25px;color:var(--ink);line-height:1;border-bottom:1px solid #999;padding-bottom:1px}
.product-name i{font-family:"Open Sans",Arial,sans-serif;font-size:9.5px;font-style:italic;margin-left:4px;color:#333}
.product-desc{font-size:12.3px;line-height:15.5px;margin-top:8px;text-align:justify}
.product-desc span{color:var(--teal)}
.product-feat{font-size:9.8px;color:var(--teal);margin-top:14px;line-height:13px}
.product-note{font-size:9.8px;color:#444;margin-top:13px;line-height:13.5px;text-align:justify}
.step-num{position:absolute;left:843px;font-family:"Open Sans",Arial,sans-serif;font-weight:700;font-size:36px;color:#2b2b2b;line-height:1}
.step-title{position:absolute;left:885px;font-family:"Bebas Neue",Impact,sans-serif;font-size:40px;color:var(--ink);line-height:1}
.step-text{position:absolute;left:887px;width:287px;font-size:17.3px;line-height:23.5px;color:#222;text-align:justify}
.step-text p+p{margin-top:4px}
.contact{font-size:14.5px;font-weight:700;font-style:italic;line-height:22px}
</style>
</head>
<body>

<svg class="band band-top" viewBox="0 0 1200 14" aria-hidden="true">
  <polygon points="8,0 195,0 181,14 8,14" fill="var(--teal)"/>
  <polygon points="195,0 620,0 606,14 181,14" fill="var(--ink)"/>
  <polygon points="620,0 1010,0 996,14 606,14" fill="var(--teal)"/>
  <polygon points="1010,0 1194,0 1194,14 996,14" fill="var(--ink)"/>
</svg>
<svg class="band band-bottom" viewBox="0 0 1200 14" aria-hidden="true">
  <polygon points="8,0 232,0 218,14 8,14" fill="var(--ink)"/>
  <polygon points="232,0 596,0 582,14 218,14" fill="var(--teal)"/>
  <polygon points="596,0 1000,0 986,14 582,14" fill="var(--ink)"/>
  <polygon points="1000,0 1194,0 1194,14 986,14" fill="var(--teal)"/>
</svg>

<!-- Panel: Our Thinking -->
<svg class="marker" style="left:27px;top:100px" viewBox="0 0 22 46" aria-hidden="true"><polygon points="0,0 22,0 22,34 11,46 0,34" fill="var(--marker)"/></svg>
<h2 class="section-title" style="left:59px;top:113px">Our Thinking</h2>
<p class="abs lead">Your experience with our product matters, every step of the way.</p>
<p class="abs value" style="top:256px"><b>EASE TO BUILD</b>:&nbsp; We believe in ease of construction using uncompromising quality.</p>
<p class="abs value" style="top:327px"><b>TRUTH IN PRODUCT</b>: We only deliver products faithful to your terms.</p>

<h2 class="section-title" style="left:107px;top:457px">How We Serve You</h2>

<svg class="serve-icon" style="top:532px" viewBox="0 0 74 76" aria-hidden="true">
  <rect x="2" y="2" width="70" height="72" fill="none" stroke="var(--ink)" stroke-width="4"/>
  <rect x="10" y="10" width="54" height="56" fill="var(--ink)"/>
  <g fill="#fff">
    <circle cx="37" cy="38" r="17"/>
    <rect x="34" y="15" width="6" height="8"/><rect x="34" y="53" width="6" height="8"/>
    <rect x="14" y="35" width="8" height="6"/><rect x="52" y="35" width="8" height="6"/>
    <rect x="34" y="15" width="6" height="8" transform="rotate(45 37 38)"/><rect x="34" y="53" width="6" height="8" transform="rotate(45 37 38)"/>
    <rect x="14" y="35" width="8" height="6" transform="rotate(45 37 38)"/><rect x="52" y="35" width="8" height="6" transform="rotate(45 37 38)"/>
  </g>
  <circle cx="37" cy="38" r="11" fill="none" stroke="var(--ink)" stroke-width="2"/>
  <path d="M26 38h22M37 27v22M37 27c-6 6-6 16 0 22M37 27c6 6 6 16 0 22" fill="none" stroke="var(--ink)" stroke-width="1.6"/>
</svg>
<h3 class="serve-title" style="top:530px">First World Tech</h3>
<p class="serve-text" style="top:557px">Italian. Danish. Chinese. We utilize first world machines for first world quality products.</p>

<svg class="serve-icon" style="top:673px" viewBox="0 0 74 76" aria-hidden="true">
  <rect x="2" y="2" width="70" height="72" fill="none" stroke="var(--ink)" stroke-width="4"/>
  <path d="M18 12l12 12" stroke="var(--ink)" stroke-width="5"/>
  <circle cx="38" cy="40" r="13" fill="none" stroke="var(--ink)" stroke-width="4"/>
  <rect x="40" y="40" width="8" height="7" fill="var(--ink)"/><rect x="50" y="40" width="8" height="7" fill="var(--ink)"/>
  <rect x="40" y="49" width="8" height="7" fill="var(--ink)"/><rect x="50" y="49" width="8" height="7" fill="var(--ink)"/>
</svg>
<h3 class="serve-title" style="top:673px">Honest Dimensions</h3>
<p class="serve-text" style="top:701px">We measure it in front of you with Spec Check. What you want is what you'll get.</p>

<svg class="serve-icon" style="top:808px" viewBox="0 0 74 76" aria-hidden="true">
  <rect x="2" y="2" width="70" height="72" fill="none" stroke="var(--ink)" stroke-width="4"/>
  <rect x="10" y="24" width="32" height="24" fill="var(--ink)"/>
  <path d="M44 30h12l8 9v9H44z" fill="var(--ink)"/>
  <circle cx="22" cy="52" r="5" fill="var(--ink)"/><circle cx="54" cy="52" r="5" fill="var(--ink)"/>
</svg>
<h3 class="serve-title" style="top:806px">2D Delivery</h3>
<p class="serve-text" style="top:837px">2 Days after-order delivery – 10 days return</p>

<!-- Panel: Our Products -->
<svg class="marker" style="left:427px;top:100px" viewBox="0 0 22 46" aria-hidden="true"><polygon points="0,0 22,0 22,34 11,46 0,34" fill="var(--marker)"/></svg>
<h2 class="section-title" style="left:459px;top:113px">Our Products</h2>

<div class="product-shot" style="top:166px;background:linear-gradient(135deg,#e9ebe6,#cfd3cb)" role="img" aria-label="Gloved hands holding welded steel wire mesh"></div>
<div class="product" style="top:166px">
  <h3 class="product-name">Wire Mesh<i>Flat the Surface</i></h3>
  <p class="product-desc"><span>Welded Steel Matting.</span> Fused by Singaporean engineering</p>
  <p class="product-feat">Features:&nbsp; True Measure</p>
  <p class="product-note">Used for: Cement Reinforcement. Finishing Construction.</p>
</div>

<div class="product-shot" style="top:331px;background:linear-gradient(135deg,#e4e6e2,#6c6f6b)" role="img" aria-label="Gloved hands drawing wire from a black coil"></div>
<div class="product" style="top:330px">
  <h3 class="product-name">BI Wire<i>Reprocess and Strengthen</i></h3>
  <p class="product-desc"><span>Cold-drawn Wire.</span> Cut by Italian Cassettes. Drawn straight-line by Chinese engineering.</p>
  <p class="product-feat">Features:&nbsp; Authentic Draw.</p>
  <p class="product-note">Used for: Concrete Pipes. Kitchenware. Furniture Export.</p>
</div>

<div class="product-shot" style="top:516px;background:linear-gradient(135deg,#f1f1f0,#ddd8d2)" role="img" aria-label="Hand holding a single steel nail"></div>
<div class="product" style="top:515px">
  <h3 class="product-name">Nails<i>Thrust and Bind</i></h3>
  <p class="product-desc"><span>Cold-formed Nails.</span> Cut &amp; formed by Danish engineering.</p>
  <p class="product-feat">Features:&nbsp; Export-Quality. Sharp Point. Round Head.</p>
  <p class="product-note">Choice:&nbsp; Common Nail. Finishing Nail.</p>
  <p class="product-note" style="margin-top:8px">Used for:&nbsp; Rough Construction. Smooth Housing.</p>
</div>

<div class="product-shot" style="top:716px;background:linear-gradient(135deg,#f2f2f1,#dcd6cf)" role="img" aria-label="Hand holding a bent coil of galvanized wire"></div>
<div class="product" style="top:714px">
  <h3 class="product-name">GI Wire<i>Bend and Shape</i></h3>
  <p class="product-desc"><span>Hot-dipped Galvanized Iron.</span> Anneal-Heated. Coated with Zinc.</p>
  <p class="product-feat" style="margin-top:20px">Features:&nbsp; Rust Protect Easy Bend.</p>
  <p class="product-note" style="margin-top:8px">Used for:&nbsp; Steel Bar Reinforcement. Industrial packaging.</p>
  <p class="product-note" style="margin-top:8px">Also available:&nbsp; Barbed Wire. Cyclone Wire. Hog Wire.</p>
</div>

<!-- Panel: How It Works -->
<svg class="marker" style="left:822px;top:100px" viewBox="0 0 22 46" aria-hidden="true"><polygon points="0,0 22,0 22,34 11,46 0,34" fill="var(--marker)"/></svg>
<h2 class="section-title" style="left:854px;top:113px">How It Works</h2>

<span class="step-num" style="top:160px">1</span>
<h3 class="step-title" style="top:162px">Order Up</h3>
<div class="step-text" style="top:201px">
  <p>Give us a hello and we'll give you a <b><i>quotation</i></b>. E-mail would also be nice. Remember: Bigger Volume = Bigger Discount.</p>
  <p class="contact" style="margin-top:2px">555-0147.<br>ferrobayfabcorp@mailvane.com</p>
</div>

<span class="step-num" style="top:376px">2</span>
<h3 class="step-title" style="top:378px">We'll Deliver</h3>
<div class="step-text" style="top:419px">
  <p>Our 10-wheelers will get to you <b><i>within 2 days</i></b> of your order.</p>
  <p>Need an update? Call us for your order's ETA.</p>
</div>

<span class="step-num" style="top:555px">3</span>
<h3 class="step-title" style="top:557px">Spec Check</h3>
<div class="step-text" style="top:603px">
  <p>We will measure the product dimensions <b><i>in front of you</i></b> when we get there.</p>
  <p style="text-align:left">No worries on your order. What you want is what you'll get.</p>
</div>

<span class="step-num" style="top:768px">4</span>
<h3 class="step-title" style="top:770px">Done!</h3>
<div class="step-text" style="top:812px;left:885px;text-align:left">
  <p>That's it! Call us for feedback.</p>
  <p>Not happy with the quality? Call us <b><i>within 10 days</i></b> for replacement.</p>
</div>

</body>
</html>
```